Versicherungsmakler sucht Corporate Design (Logo, Visitenkarte, Briefpapier)
Zielgruppe
Optimale Beratung speziell auf die Zielgruppe werdende Eltern/Junge Familie abgestimmt.
Es geht darum, welche Absicherung (Versicherung, Vorsorge, Sparprodukte) gerade für diese spezielle Zielgruppe (und dort im Besonderen für die Kinder) essentiell ist. Leider werden diesen Kunden von Kollegen oft falsche beraten oder erhalten unbrauchbare oder zu teure Produkte. Mir ist es wichtig nur die richtigen und wichtigen Produkte zu vermitteln. Dies kann ich sehr gut beurteilen, weil ich selbst 2facher Familienvater bin (2 Jungs im Alter von1x 2 Jahren und1x 5 Monaten). Das ganze soll unabhängig von jeglichen Interessen der Versicherungswirtschaft und derer Unternehmen erfolgen, d.h. vollkommen auf die Anforderungen und Bedürfnisse des Kunden abgestimmt!!!
Aufgabenstellung
Ich suche nun noch einen zusätzlichen Markenauftritt für "NestWohl - klug geplant, sicher gebettet" (Logo, Visitenkarte, Briefpapier) für die o.g. spezielle Zielgruppe "Junge Familie/werdende Eltern". Der Fokus liegt auf der Vorsorge und Absicherung der Kinder.

```html
<!DOCTYPE html>
<html lang="de">
<head>
<meta charset="utf-8">
<title>NestWohl – Visitenkarte</title>
<link rel="stylesheet" href="https://fonts.googleapis.com/css2?family=Open+Sans:wght@400;600;700&family=Merriweather:wght@300;400&display=swap">
<style>
  :root {
    --bg: #e6e7e9;
    --card: #ffffff;
    --card-front: #f4f4f2;
    --green: #8cc63f;
    --mid: #3fb58a;
    --teal: #17a6c9;
    --brand: #1f9a72;
    --ink: #2b2b2b;
    --white: #ffffff;
  }
  * { margin: 0; padding: 0; box-sizing: border-box; }
  html, body { width: 1200px; height: 873px; overflow: hidden; }
  body {
    background: var(--bg);
    position: relative;
    font-family: "Merriweather", Georgia, serif;
    color: var(--ink);
  }
  .card {
    position: absolute;
    top: 268px;
    width: 520px;
    height: 336px;
    box-shadow: 0 6px 18px rgba(0,0,0,.15);
    overflow: hidden;
  }
  .card--front { left: 45px; background: var(--card-front); }
  .card--back { left: 635px; background: var(--card); }

  /* front */
  .brand {
    position: absolute;
    left: 0; right: 0; top: 92px;
    display: flex; justify-content: center; align-items: center; gap: 14px;
  }
  .brand__dot { width: 34px; height: 34px; border-radius: 50%; background: var(--brand); }
  .brand__name {
    font-family: "Open Sans", Arial, sans-serif;
    font-weight: 700; font-size: 44px; letter-spacing: 1px;
    color: var(--brand);
  }
  .tagline {
    position: absolute; left: 0; right: 0; top: 178px;
    text-align: center; font-size: 22px; font-weight: 400;
  }

  /* back */
  .band {
    position: absolute; left: 0; top: 0; width: 100%; height: 128px;
    background: linear-gradient(100deg, var(--green) 0%, var(--mid) 55%, var(--teal) 100%);
  }
  .band__brand {
    position: absolute; left: 26px; top: 44px;
    display: flex; align-items: center; gap: 10px;
  }
  .band__dot { width: 22px; height: 22px; border-radius: 50%; background: var(--white); }
  .band__name {
    font-family: "Open Sans", Arial, sans-serif;
    font-weight: 600; font-size: 22px; color: var(--white);
  }
  .person {
    position: absolute; right: 26px; top: 54px; text-align: right; color: var(--white);
  }
  .person__name {
    font-family: "Open Sans", Arial, sans-serif;
    font-size: 24px; letter-spacing: 3px; text-transform: uppercase;
  }
  .person__role { font-size: 13px; font-weight: 300; margin-top: 2px; }
  .contact { position: absolute; font-size: 12.5px; line-height: 1.55; }
  .contact--address { left: 26px; top: 160px; }
  .contact--phone { left: 26px; top: 212px; }
  .contact--web { right: 26px; bottom: 30px; }
</style>
</head>
<body>
  <section class="card card--front">
    <div class="brand">
      <span class="brand__dot"></span>
      <span class="brand__name">NESTWOHL</span>
    </div>
    <p class="tagline">Klug geplant, sicher gebettet.</p>
  </section>

  <section class="card card--back">
    <div class="band">
      <div class="band__brand">
        <span class="band__dot"></span>
        <span class="band__name">NestWohl</span>
      </div>
      <div class="person">
        <p class="person__name">Jonas Brenner</p>
        <p class="person__role">Geschäftsführung</p>
      </div>
    </div>
    <p class="contact contact--address">Lindenweg 17<br>48215 Feldstadt</p>
    <p class="contact contact--phone">Tel.: +49 (0) 56 78 21 40<br>Fax: +49 (0) 56 78 21 42</p>
    <p class="contact contact--web">Email: info@nestwohl.de<br>www.nestwohl.de</p>
  </section>
</body>
</html>
```